Kellow Family Law, legal technician needs a website and design

I need a website for a family law practice. I specialize in collaborative law, unbundled services, and mediation. The website must contain my company logo (file attached), and the website must be a mixture of my personality and my profession. I have attached additional information to explain my personality and profession.

Target Market(s)

Lower through middle-class (income level up to $200,000 per year)

Coding

Coded - Design and coding required

Number of Pages Required

1 page

Requirements
Must have
• Must have enough pages to cover required content. I submitted below some content about the collaborative law process. All of the content is not necessary. However, the website must have enough content to clearly describe the services I offer. Use your professionalism and judgment regarding font, font size, etc.

```html
<!DOCTYPE html>
<html lang="en">
<head>
<meta charset="utf-8">
<title>Kellow Family Law</title>
<link href="https://fonts.googleapis.com/css2?family=Frank+Ruhl+Libre:wght@400;500&family=Arimo:ital@0;1&display=swap" rel="stylesheet">
<style>
:root{
  --navy:#03061f;
  --navy-2:#0a0d33;
  --gold:#857733;
  --gold-bright:#b3ad3b;
  --olive-btn:#aaa534;
  --white:#ffffff;
  --ink:#1b1b2a;
  --grey-text:#555;
  --light:#e7e7e7;
}
*{box-sizing:border-box;margin:0;padding:0}
html,body{width:1200px;height:4153px;overflow:hidden}
body{font-family:"Arimo",Arial,sans-serif;color:var(--ink);background:#fff;position:relative}
.serif{font-family:"Frank Ruhl Libre",Georgia,serif}
section,header,footer{position:absolute;left:0;width:1200px}
.abs{position:absolute}

/* header */
.site-header{top:0;height:142px;background:var(--navy);border-bottom:2px solid #9a9aa6}
.brand{left:111px;top:40px;display:flex;align-items:center;gap:14px}
.brand-mark{width:44px;height:44px;border:2px solid var(--gold-bright)}
.brand-name{font-family:"Frank Ruhl Libre",serif;font-size:25px;color:var(--gold-bright);letter-spacing:1px;text-transform:uppercase;line-height:1}
.top-contact{top:20px;display:flex;align-items:center;gap:12px;font-family:"Frank Ruhl Libre",serif}
.top-contact .ico{width:40px;height:40px;border-radius:50%;background:#1b1e3f;display:flex;align-items:center;justify-content:center}
.top-contact small{display:block;color:#fff;font-size:14px}
.top-contact span{color:var(--gold-bright);font-size:17px}
.main-nav{top:97px;left:437px;display:flex;gap:0;font-family:"Frank Ruhl Libre",serif;font-size:14px;color:#fff}
.main-nav a{color:#fff;text-decoration:none;position:absolute;white-space:nowrap}
.main-nav a.active{color:var(--gold-bright)}

/* hero */
.hero{top:142px;height:738px;background:radial-gradient(ellipse at 50% 40%,#4a4540 0%,#2a2a2e 45%,#15161c 100%);text-align:center;color:#fff}
.hero h1{position:absolute;top:330px;width:100%;font-family:"Frank Ruhl Libre",serif;font-weight:500;font-size:50px;color:var(--gold-bright);text-transform:uppercase}
.hero p{position:absolute;top:412px;width:100%;font-family:"Frank Ruhl Libre",serif;font-size:24px;line-height:44px;text-transform:uppercase}
.btn{display:inline-flex;align-items:center;justify-content:center;font-family:"Frank Ruhl Libre",serif;text-transform:uppercase;border-radius:40px;text-decoration:none}
.hero .btn{position:absolute;left:511px;top:519px;width:178px;height:65px;background:var(--olive-btn);color:#fff;font-size:20px}

/* section titles */
.sec-title{position:absolute;width:100%;text-align:center;font-family:"Frank Ruhl Libre",serif;font-size:34px;text-transform:uppercase;font-weight:400}
.sec-rule{position:absolute;left:577px;width:46px;height:2px;background:var(--gold)}

/* services */
.services{top:880px;height:719px}
.service-card{position:absolute;top:154px;width:307px;height:461px;border-radius:16px;overflow:hidden;color:#fff;text-align:center}
.service-card .photo{height:221px}
.service-card h3{margin-top:30px;font-family:"Frank Ruhl Libre",serif;font-weight:400;font-size:18px;text-transform:uppercase}
.service-card p{margin:14px auto 0;width:260px;font-size:13px;line-height:26px}
.service-card .btn{margin-top:27px;width:147px;height:50px;border:1px solid #fff;color:#fff;font-size:15px}
.card-navy{background:var(--navy)}
.card-gold{background:var(--gold)}

/* about */
.about{top:1599px;left:111px;width:978px;height:493px;background:#fff;box-shadow:0 0 12px rgba(0,0,0,.15)}
.about .photo{position:absolute;left:0;top:0;width:481px;height:493px;background:linear-gradient(120deg,#6b4a2e,#2c2a35 55%,#8b6a3a)}
.about .label{position:absolute;left:534px;top:60px;font-family:"Frank Ruhl Libre",serif;font-size:30px;text-transform:uppercase}
.about h2{position:absolute;left:534px;top:102px;font-family:"Frank Ruhl Libre",serif;font-weight:400;font-size:35px;color:var(--gold);text-transform:uppercase}
.about p{position:absolute;left:536px;top:165px;width:405px;font-size:13px;line-height:25.6px;color:var(--grey-text)}
.about .btn{position:absolute;left:536px;top:372px;width:172px;height:58px;background:var(--navy);color:#fff;font-size:18px}

/* testimonials */
.testimonials{top:2173px;height:576px;background:linear-gradient(90deg,#7a6d2e,#8a7b36 50%,#7a6d2e);color:#fff;text-align:center}
.testimonials .quote-mark{position:absolute;top:140px;width:100%;font-family:"Frank Ruhl Libre",serif;font-size:120px;line-height:1;height:80px}
.testimonials blockquote{position:absolute;left:284px;top:253px;width:632px;font-style:italic;font-size:17px;line-height:32px}
.avatar{position:absolute;left:494px;top:417px;width:88px;height:88px;border-radius:50%;background:linear-gradient(#c9a88a,#5a3f30);border:3px solid #fff}
.reviewer{position:absolute;left:597px;top:438px;text-align:left;font-family:"Frank Ruhl Libre",serif;font-size:18px;text-transform:uppercase}
.stars{position:absolute;left:597px;top:466px;display:flex;gap:4px}

/* team */
.team{top:2749px;height:635px}
.member{position:absolute;top:143px;width:290px;height:411px}
.member .photo{width:290px;height:315px}
.member .info{position:absolute;left:39px;top:276px;width:215px;height:135px;background:#fff;box-shadow:0 0 6px rgba(0,0,0,.18);text-align:center}
.member h4{margin-top:14px;font-family:"Frank Ruhl Libre",serif;font-weight:400;font-size:18px}
.member .role{margin-top:4px;font-size:13px;color:#777}
.member .social{margin-top:16px;display:flex;justify-content:center;gap:6px}
.member .social i{width:33px;height:33px;border:1px solid #999;border-radius:50%;display:block}

/* contact */
.contact{top:3384px;height:436px;background:linear-gradient(100deg,#f1f1f1,#dcdcdc 60%,#ececec)}
.contact p.lead{position:absolute;top:88px;width:100%;text-align:center;font-size:14px;color:#444}
.field{position:absolute;background:#fff;border:1px solid #bbb;font-family:"Frank Ruhl Libre",serif;font-size:14px;color:#333;padding:14px 16px}
.contact .btn{position:absolute;left:518px;top:336px;width:164px;height:56px;background:var(--gold);color:#fff;font-size:15px}

/* footer */
.site-footer{top:3820px;height:333px;background:var(--navy);color:#fff;font-family:"Frank Ruhl Libre",serif;font-size:14px}
.vline{position:absolute;top:60px;width:1px;height:130px;background:#3a3d5c}
.footer-rule{position:absolute;left:111px;top:242px;width:978px;height:1px;background:#3a3d5c}
.copyright{position:absolute;top:276px;width:100%;text-align:center;font-size:16px}
.circle-link{position:absolute;top:150px;width:42px;height:42px;border:2px solid #fff;border-radius:50%}
.live-chat{position:absolute;left:1148px;top:84px;width:60px;height:148px;background:var(--olive-btn);border-radius:10px 0 0 10px}
.live-chat span{position:absolute;left:14px;top:120px;transform:rotate(-90deg);transform-origin:left top;font-size:14px;white-space:nowrap}
</style>
</head>
<body>

<header class="site-header">
  <div class="brand abs"><span class="brand-mark"></span><span class="brand-name">Kellow Family Law</span></div>
  <div class="top-contact abs" style="left:702px">
    <div class="ico"><svg width="18" height="18" viewBox="0 0 24 24" fill="none" stroke="#b3ad3b" stroke-width="2"><path d="M5 3h4l2 5-3 2a11 11 0 0 0 6 6l2-3 5 2v4a2 2 0 0 1-2 2A17 17 0 0 1 3 5a2 2 0 0 1 2-2z"/></svg></div>
    <div><small>Call Us</small><span>000.121.1231</span></div>
  </div>
  <div class="top-contact abs" style="left:880px">
    <div class="ico"><svg width="18" height="14" viewBox="0 0 24 18" fill="none" stroke="#b3ad3b" stroke-width="2"><rect x="1" y="1" width="22" height="16"/><path d="M1 1l11 9 11-9"/></svg></div>
    <div><small>Email</small><span>info@company.com</span></div>
  </div>
  <nav class="main-nav abs">
    <a class="active" style="left:0">HOME</a>
    <a style="left:92px">ABOUT US</a>
    <a style="left:211px">SERVICES</a>
    <a style="left:326px">WHAT WE DO</a>
    <a style="left:469px">NEWS</a>
    <a style="left:558px">CONTACT US</a>
  </nav>
</header>

<section class="hero" role="img" aria-label="Photo of smiling lawyers meeting with clients at a desk">
  <h1>Kellow Family Law</h1>
  <p>Collaborative law and unbundled legal services in<br>King County, Washington State</p>
  <a class="btn">Read More</a>
</section>

<section class="services">
  <h2 class="sec-title" style="top:58px">Our Services</h2>
  <div class="sec-rule" style="top:116px"></div>
  <article class="service-card card-navy" style="left:111px">
    <div class="photo" role="img" aria-label="Photo of a business team shaking hands at a meeting table" style="background:linear-gradient(135deg,#d9e4e6,#7d8a93)"></div>
    <h3>Collaborative Law</h3>
    <p>Sed ut perspiciatis unde omnis iste natus error sit voluptatem accusantium dolorem vitae dicta sunt explicabo.</p>
    <a class="btn">Read More</a>
  </article>
  <article class="service-card card-gold" style="left:447px">
    <div class="photo" role="img" aria-label="Photo of hands passing a pen over documents" style="background:linear-gradient(135deg,#e6e6e6,#6a6a6e)"></div>
    <h3>Unbundled Services</h3>
    <p>Sed ut perspiciatis unde omnis iste natus error sit voluptatem accusantium dolorem vitae dicta sunt explicabo.</p>
    <a class="btn">Read More</a>
  </article>
  <article class="service-card card-navy" style="left:781px">
    <div class="photo" role="img" aria-label="Photo of a consultation with paperwork on a desk" style="background:linear-gradient(135deg,#b8b0a8,#3a3234)"></div>
    <h3>Mediation</h3>
    <p>Sed ut perspiciatis unde omnis iste natus error sit voluptatem accusantium dolorem vitae dicta sunt explicabo.</p>
    <a class="btn">Read More</a>
  </article>
</section>

<section class="about">
  <div class="photo" role="img" aria-label="Photo of a lawyer reading a book in a library"></div>
  <div class="label">About</div>
  <h2>Kellow Family Law</h2>
  <p>Nemo enim ipsam voluptatem quia voluptas sit aspernatur aut odit aut fugit, sed quia consequuntur magni dolores eos qui ratione vol uptatem sequi nesciunt. Neque porro quisquam est, qui dolorem ipsum quia dolor sit amet, consectetur, adipisci velit, sed quia non numquam eius modi tempora incidunt ut labore et dolore magnam aliquam quaerat voluptatem.Ut enim ad minima veniam, quis nost rum exercitationem ullam corporis suscipit laboriosam</p>
  <a class="btn">Read More</a>
</section>

<section class="testimonials">
  <h2 class="sec-title" style="top:80px;color:#fff">Testimonials</h2>
  <div class="sec-rule" style="top:137px;background:#fff"></div>
  <div class="quote-mark">&ldquo;</div>
  <svg class="abs" style="left:166px;top:223px" width="30" height="134" viewBox="0 0 30 134" fill="none" stroke="#fff" stroke-width="2"><path d="M28 1L2 67l26 66"/></svg>
  <svg class="abs" style="left:1014px;top:223px" width="30" height="134" viewBox="0 0 30 134" fill="none" stroke="#fff" stroke-width="2"><path d="M2 1l26 66-26 66"/></svg>
  <blockquote>Sed ut perspiciatis unde omnis iste natus error sit voluptatem accusantium dolorem que laudantium, totam rem aperiam, eaque ipsa quae ab illo inventore veritatis et quasi architecto beatae vitae dicta sunt explicabo. Nemo enim ipsam voluptatem quia voluptas sit aspernatur aut odit aut fugit, sed quia consequuntur magni dolores eos qui ratione voluptatem sequi nesciunt.</blockquote>
  <div class="avatar" role="img" aria-label="Client portrait"></div>
  <div class="reviewer">Avery Lane</div>
  <div class="stars">
    <svg width="88" height="16" viewBox="0 0 88 16" fill="#fff"><g id="s"><path d="M8 0l2.4 5 5.6.6-4.2 3.8 1.2 5.6L8 12.2 3 15l1.2-5.6L0 5.6 5.6 5z"/></g><use href="#s" x="18"/><use href="#s" x="36"/><use href="#s" x="54"/><use href="#s" x="72"/></svg>
  </div>
</section>

<section class="team">
  <h2 class="sec-title" style="top:42px">Our Team</h2>
  <div class="sec-rule" style="top:104px"></div>
  <article class="member" style="left:111px">
    <div class="photo" role="img" aria-label="Portrait of a team member in a dark suit" style="background:linear-gradient(135deg,#b87f4d,#4a3a36)"></div>
    <div class="info"><h4>Avery Lane</h4><div class="role">Family Law</div><div class="social"><i></i><i></i><i></i></div></div>
  </article>
  <article class="member" style="left:455px">
    <div class="photo" role="img" aria-label="Portrait of a team member in a navy suit" style="background:linear-gradient(135deg,#c8c3b0,#2e3a55)"></div>
    <div class="info"><h4>Avery Lane</h4><div class="role">Family Law</div><div class="social"><i></i><i></i><i></i></div></div>
  </article>
  <article class="member" style="left:797px">
    <div class="photo" role="img" aria-label="Portrait of a team member in a grey jacket" style="background:linear-gradient(135deg,#8a6a55,#2e2a2c)"></div>
    <div class="info"><h4>Avery Lane</h4><div class="role">Family Law</div><div class="social"><i></i><i></i><i></i></div></div>
  </article>
</section>

<section class="contact">
  <h2 class="sec-title" style="top:30px">Contact Us</h2>
  <p class="lead">Sed ut perspiciatis unde omnis iste natus error sit voluptatem accusantium doloremque</p>
  <div class="field" style="left:261px;top:131px;width:336px;height:48px">First Name :</div>
  <div class="field" style="left:605px;top:131px;width:335px;height:48px">Last Name :</div>
  <div class="field" style="left:261px;top:192px;width:336px;height:48px">Email :</div>
  <div class="field" style="left:605px;top:192px;width:335px;height:48px">Phone :</div>
  <div class="field" style="left:261px;top:253px;width:679px;height:68px">Message :</div>
  <a class="btn">Submit</a>
</section>

<footer class="site-footer">
  <div class="brand abs" style="left:163px;top:100px"><span class="brand-mark"></span><span class="brand-name">Kellow Family Law</span></div>
  <div class="vline" style="left:447px"></div>
  <svg class="abs" style="left:492px;top:80px" width="16" height="22" viewBox="0 0 16 22" fill="none" stroke="#fff" stroke-width="1.5"><path d="M8 21s7-7.5 7-13A7 7 0 0 0 1 8c0 5.5 7 13 7 13z"/><circle cx="8" cy="8" r="2.5"/></svg>
  <div class="abs" style="left:531px;top:74px;line-height:23px">Address<br>P.O. Box 383 Lorem Ipsum<br>Dummy MA 02471</div>
  <span class="circle-link" style="left:531px"></span>
  <span class="circle-link" style="left:584px"></span>
  <div class="vline" style="left:777px"></div>
  <svg class="abs" style="left:830px;top:84px" width="20" height="20" viewBox="0 0 24 24" fill="none" stroke="#fff" stroke-width="1.5"><path d="M5 3h4l2 5-3 2a11 11 0 0 0 6 6l2-3 5 2v4a2 2 0 0 1-2 2A17 17 0 0 1 3 5a2 2 0 0 1 2-2z"/></svg>
  <div class="abs" style="left:869px;top:74px;line-height:26px">Phone:<br>000.121.1231</div>
  <svg class="abs" style="left:830px;top:146px" width="22" height="16" viewBox="0 0 24 18" fill="none" stroke="#fff" stroke-width="1.5"><rect x="1" y="1" width="22" height="16"/><path d="M1 1l11 9 11-9"/></svg>
  <div class="abs" style="left:869px;top:144px;line-height:26px">Email :<br>info@company.com</div>
  <div class="footer-rule"></div>
  <div class="copyright">Kellow Family Law © 2021.All Rights Reserved.</div>
  <div class="live-chat"><span>LIVE CHAT</span></div>
</footer>

</body>
</html>
```